Maple Hollow Summer Swim Bag Tag Design

Hello!

We are looking to design a 2-sided bag tag for a children's summer swim team. Colors should be blue, white, pink. May also use a lighter blue or navy as an accent if needed. Attached are 2 files showing the look/feel of some of our other items. The bag tag would need to be in line with this same look.

Copy: Maple Hollow Otters Swim 2026
#paddlesout

The copy can be both on one side, or split between the 2 sides, either works. We are flexible! Needs to incorporate the 2026 logo into the design.

```html
<!DOCTYPE html>
<html lang="en">
<head>
<meta charset="utf-8">
<title>Maple Hollow Summer Swim Bag Tag</title>
<link rel="stylesheet" href="https://fonts.googleapis.com/css2?family=Archivo:wght@700;800;900&display=swap">
<style>
  :root {
    --team-blue: #1c48a6;
    --team-pink: #f0508e;
    --sky-blue: #3b9be8;
    --white: #ffffff;
    --page: #ffffff;
  }
  * { box-sizing: border-box; margin: 0; padding: 0; }
  html, body {
    width: 1200px; height: 1200px; overflow: hidden;
    background: var(--page);
    font-family: "Archivo", "Arial Narrow", sans-serif;
  }
  .sheet { position: relative; width: 1200px; height: 1200px; }
  .tag {
    position: absolute; top: 168px;
    width: 498px; height: 872px;
    background: var(--team-blue);
    border-radius: 26px;
    overflow: hidden;
  }
  .tag--front { left: 74px; }
  .tag--back { left: 629px; }
  .tag__slot {
    position: absolute; top: 23px; left: 50%;
    width: 120px; height: 34px; margin-left: -60px;
    background: var(--page); border-radius: 9px;
  }
  .side-label {
    position: absolute; top: 1078px; width: 498px;
    text-align: center; color: var(--team-blue);
    font-weight: 800; font-size: 32px; letter-spacing: 0.5px;
  }
  .side-label--front { left: 74px; }
  .side-label--back { left: 629px; }

  /* Year mark */
  .year-mark { position: absolute; left: 0; top: 0; width: 100%; height: 270px; }
  .year-mark__digit {
    position: absolute; font-weight: 900; font-size: 88px; line-height: 1;
    color: var(--white); letter-spacing: -2px;
  }
  .year-mark__digit--two-top { left: 196px; top: 92px; }
  .year-mark__digit--two-bottom { left: 200px; top: 176px; }
  .year-mark__digit--six { left: 256px; top: 176px; color: var(--team-pink); }
  .year-mark__badge {
    position: absolute; left: 246px; top: 100px;
    width: 70px; height: 70px; border-radius: 50%;
    background: var(--white);
    display: flex; align-items: center; justify-content: center;
    text-align: center;
    color: var(--team-blue); font-weight: 800; font-size: 10px; line-height: 1.05;
  }

  /* Team name */
  .team-name {
    position: absolute; left: 0; top: 280px; width: 100%;
    text-align: center; font-weight: 800; text-transform: uppercase;
    line-height: 1.1; letter-spacing: -1px; color: var(--white);
  }
  .team-name__line { display: block; font-size: 86px; }
  .team-name__line--accent { color: var(--team-pink); }
  .team-name__line--swim { font-size: 156px; letter-spacing: -2px; line-height: 1; }

  .waves { position: absolute; left: 0; width: 100%; }
  .waves--front { top: 728px; height: 144px; }
  .waves--back { top: 590px; height: 282px; }

  /* Back hashtag */
  .mascot-art {
    position: absolute; left: 250px; top: 150px;
    width: 210px; height: 170px; border-radius: 40px;
    background: radial-gradient(ellipse at 55% 45%, rgba(240,80,142,0.75) 0%, rgba(240,80,142,0.35) 50%, rgba(28,72,166,0) 100%);
  }
  .hashtag {
    position: absolute; left: 0; top: 300px; width: 100%;
    font-weight: 900; line-height: 1; letter-spacing: -2px;
  }
  .hashtag__main {
    display: block; padding-left: 28px;
    font-size: 88px; color: var(--white);
  }
  .hashtag__tail {
    display: block; padding-right: 40px; margin-top: 4px;
    text-align: right; font-size: 130px; color: var(--team-pink);
  }
</style>
</head>
<body>
<main class="sheet">

  <section class="tag tag--front" aria-label="Bag tag front">
    <div class="tag__slot"></div>
    <div class="year-mark" aria-label="2026">
      <span class="year-mark__digit year-mark__digit--two-top">2</span>
      <span class="year-mark__badge">MAPLE<br>HOLLOW</span>
      <span class="year-mark__digit year-mark__digit--two-bottom">2</span>
      <span class="year-mark__digit year-mark__digit--six">6</span>
    </div>
    <h1 class="team-name">
      <span class="team-name__line">Maple</span>
      <span class="team-name__line">Hollow</span>
      <span class="team-name__line team-name__line--accent">Otters</span>
      <span class="team-name__line team-name__line--swim">Swim</span>
    </h1>
    <svg class="waves waves--front" viewBox="0 0 498 144" preserveAspectRatio="none" aria-hidden="true">
      <path d="M0 30 C90 10 170 40 260 28 C340 18 400 8 498 12 L498 26 C400 24 340 34 260 44 C170 56 90 26 0 44 Z" fill="var(--team-pink)"/>
      <path d="M0 58 C100 40 180 72 280 60 C370 50 430 36 498 40 L498 62 C430 58 370 74 280 84 C180 96 100 64 0 80 Z" fill="var(--white)"/>
      <path d="M0 96 C110 80 200 110 300 98 C380 88 440 76 498 80 L498 100 C440 98 380 112 300 122 C200 134 110 106 0 118 Z" fill="var(--sky-blue)"/>
    </svg>
  </section>

  <section class="tag tag--back" aria-label="Bag tag back">
    <div class="tag__slot"></div>
    <div class="mascot-art" role="img" aria-label="Leaping pink otter with white and blue water splashes"></div>
    <p class="hashtag">
      <span class="hashtag__main">#paddles</span>
      <span class="hashtag__tail">out</span>
    </p>
    <svg class="waves waves--back" viewBox="0 0 498 282" preserveAspectRatio="none" aria-hidden="true">
      <path d="M0 60 C90 30 170 70 260 50 C350 30 420 20 498 10 L498 34 C420 44 350 56 260 78 C170 98 90 60 0 88 Z" fill="var(--team-pink)"/>
      <path d="M0 100 C100 70 190 110 290 90 C380 72 440 60 498 56 L498 84 C440 90 380 102 290 120 C190 140 100 102 0 128 Z" fill="var(--sky-blue)"/>
      <path d="M0 140 C110 110 200 150 300 132 C390 116 450 104 498 100 L498 124 C450 130 390 142 300 158 C200 176 110 142 0 166 Z" fill="var(--white)"/>
      <path d="M0 180 C110 150 210 192 310 172 C400 156 450 146 498 142 L498 168 C450 172 400 184 310 200 C210 220 110 186 0 208 Z" fill="var(--team-pink)"/>
      <path d="M0 222 C120 194 220 234 320 214 C400 200 450 190 498 188 L498 214 C450 216 400 228 320 244 C220 262 120 228 0 252 Z" fill="var(--sky-blue)"/>
    </svg>
  </section>

  <p class="side-label side-label--front">FRONT</p>
  <p class="side-label side-label--back">BACK</p>

</main>
</body>
</html>
```